I need a business card design for a Boutique Pilates studio.

I would like to see designs similar to the one that I have uploaded.
thinking between two slogans:
'No ordinary place'
'Not so ordinary'

Contact Information for Business Card

KiVa Pilates

```html
<!DOCTYPE html>
<html lang="en">
<head>
<meta charset="utf-8">
<title>KiVa Pilates – Business Card</title>
<link rel="stylesheet" href="https://fonts.googleapis.com/css2?family=Oswald:wght@400;500&display=swap">
<style>
  :root {
    --page: #f4f5f6;
    --card: #41484a;
    --panel: #484747;
    --gold: #f2d31b;
  }
  * { box-sizing: border-box; margin: 0; padding: 0; }
  html, body { width: 1020px; height: 1200px; overflow: hidden; background: var(--page); }
  body {
    display: flex; flex-direction: column; align-items: center; justify-content: center;
    gap: 80px; font-family: "Oswald", sans-serif; color: var(--gold);
  }
  .card {
    position: relative; width: 760px; height: 434px; background: var(--card);
  }
  .panel { position: absolute; background: var(--panel); }
  .notch { position: absolute; background: var(--card); }
  .brand-name {
    position: absolute; left: 0; right: 0; text-align: center;
    font-weight: 400; font-size: 66px; letter-spacing: 3px; line-height: 1;
  }
  .tagline {
    position: absolute; left: 0; right: 0; text-align: center;
    font-weight: 500; font-size: 21px; letter-spacing: 4px; line-height: 1;
  }
  /* front */
  .card--front .panel { left: 52px; top: 76px; width: 655px; height: 281px; }
  .card--front .notch { left: 221px; top: 281px; width: 342px; height: 76px; }
  .card--front .brand-name { top: 160px; }
  .card--front .tagline { top: 291px; }
  /* back */
  .card--back .panel { left: 105px; top: 47px; width: 553px; height: 235px; }
  .card--back .notch { left: 245px; top: 218px; width: 290px; height: 64px; }
  .card--back .brand-name { top: 96px; }
  .card--back .tagline { top: 225px; font-size: 19px; letter-spacing: 2px; }
  .contact-list { list-style: none; }
  .contact-item {
    position: absolute; display: flex; align-items: center; gap: 12px;
    font-size: 15px; font-weight: 400; letter-spacing: 0.3px; line-height: 1;
  }
  .contact-item svg { width: 18px; height: 18px; fill: var(--gold); flex: none; }
  .contact-item--address { left: 147px; top: 301px; }
  .contact-item--email   { left: 147px; top: 342px; }
  .contact-item--phone   { left: 405px; top: 301px; }
  .contact-item--web     { left: 405px; top: 342px; }
</style>
</head>
<body>
  <section class="card card--front" aria-label="Business card front">
    <div class="panel"></div>
    <div class="notch"></div>
    <h1 class="brand-name">KiVa Pilates</h1>
    <p class="tagline">NOT SO ORDINARY</p>
  </section>

  <section class="card card--back" aria-label="Business card back">
    <div class="panel"></div>
    <div class="notch"></div>
    <h2 class="brand-name">KiVa Pilates</h2>
    <p class="tagline">NO ORDINARY PLACE</p>
    <ul class="contact-list">
      <li class="contact-item contact-item--address">
        <svg viewBox="0 0 24 24" aria-hidden="true"><path d="M12 2a7 7 0 0 0-7 7c0 5.2 7 13 7 13s7-7.8 7-13a7 7 0 0 0-7-7zm0 9.5A2.5 2.5 0 1 1 12 6.5a2.5 2.5 0 0 1 0 5z"/></svg>
        <span>XXXX-XXXXX-XXXXXXXX</span>
      </li>
      <li class="contact-item contact-item--email">
        <svg viewBox="0 0 24 24" aria-hidden="true"><path d="M2 5h20v14H2z M3.5 6.5 12 13l8.5-6.5" fill="none" stroke="#f2d31b" stroke-width="0"/><path d="M2 5h20v2.2l-10 7-10-7z"/><path d="M2 9.6l10 7 10-7V19H2z"/></svg>
        <span>XXXXX-X-XXXXXXXXXXX</span>
      </li>
      <li class="contact-item contact-item--phone">
        <svg viewBox="0 0 24 24" aria-hidden="true"><path d="M7 1h10a2 2 0 0 1 2 2v18a2 2 0 0 1-2 2H7a2 2 0 0 1-2-2V3a2 2 0 0 1 2-2zm0 3v14h10V4zm5 15.2a1.2 1.2 0 1 0 0 2.4 1.2 1.2 0 0 0 0-2.4z"/></svg>
        <span>XXXX-XXXXX-XXX</span>
      </li>
      <li class="contact-item contact-item--web">
        <svg viewBox="0 0 24 24" aria-hidden="true" fill="none" stroke="#f2d31b" stroke-width="1.8" style="fill:none"><circle cx="12" cy="12" r="9.5"/><ellipse cx="12" cy="12" rx="4" ry="9.5"/><path d="M2.5 12h19M4 7h16M4 17h16"/></svg>
        <span>XXX-XXX-XXXXXXXXXXX</span>
      </li>
    </ul>
  </section>
</body>
</html>
```